Noorbel Trust Ramazan Iftari Program

You can get more info about our organzation on [url removed, login to view]
Keep the logo colors and fonts

We are promoting to start an Iftari Program for Ramazan.
- We will be giving Iftaris & Dinner in different Masajids in Karachi
- Last 10 nights Sehri also
- Iftari will be followed with a lecture to motivate
- INCLUDE THIS ON TOP "
Whoever offers meal to a Muslim at the time of iftar they receives as much reward as that Muslim has earned. Nothing becomes less of the reward of those offered meal to. (QaswarĂ®, Sawm: 82; Ibn-i Rashkar, Siyam: 40)"
- Account Info : 02930700416781 Noorbel Trust - Sadqa Qardosh Bank Limited, Gulmarvi Branch, Karachi. Once deposited please email us at donations@[url removed, login to view] so that we can provide you with an official receipt.

Contact : Sameer Hotak +92 321 5580634 for further details

```html
<!DOCTYPE html>
<html lang="en">
<head>
<meta charset="utf-8">
<title>Noorbel Trust Ramazan Iftari Program</title>
<link rel="stylesheet" href="https://fonts.googleapis.com/css2?family=Cinzel:wght@500&family=Open+Sans:wght@400;600;700&display=swap">
<style>
  :root {
    --cream: #f7efe3;
    --pattern: #eadbc4;
    --orange: #ef7b30;
    --orange-deep: #ea6e1f;
    --orange-soft: #f6a56c;
    --green-box: #a2c764;
    --green-text: #2b531b;
    --light-text: #fff4dc;
    --dark-text: #161616;
    --white: #ffffff;
    --brand-grey: #707276;
  }
  * { margin: 0; padding: 0; box-sizing: border-box; }
  html, body { width: 849px; height: 1200px; overflow: hidden; background: var(--cream); }
  .poster {
    position: relative;
    width: 849px;
    height: 1200px;
    overflow: hidden;
    font-family: "Open Sans", sans-serif;
  }
  .backdrop-pattern {
    position: absolute; inset: 0;
    background: radial-gradient(circle at 50% 40%, var(--cream), var(--pattern));
  }
  .mosque-silhouette {
    position: absolute;
    left: 71px; top: 38px;
    width: 712px; height: 298px;
    background: linear-gradient(180deg, rgba(239,123,48,0.35) 0%, var(--orange-soft) 35%, var(--orange) 100%);
    border-radius: 46% 46% 0 0 / 30% 30% 0 0;
  }
  .brand {
    position: absolute;
    left: 205px; top: 78px;
    display: flex; align-items: center; gap: 10px;
  }
  .brand-dot {
    width: 26px; height: 26px; border-radius: 50%;
    background: var(--brand-grey);
  }
  .brand-name {
    font-family: "Open Sans", sans-serif;
    font-weight: 400;
    font-size: 54px;
    color: var(--brand-grey);
    line-height: 1;
  }
  .panel {
    position: absolute;
    left: 71px; top: 335px;
    width: 712px; height: 865px;
    background: var(--orange);
  }
  .headline {
    position: absolute;
    left: 71px; top: 370px; width: 712px;
    text-align: center;
    font-family: "Cinzel", serif;
    font-weight: 500;
    font-size: 34px;
    line-height: 48px;
    letter-spacing: 1px;
    color: var(--light-text);
  }
  .hadith {
    position: absolute;
    left: 69px; top: 500px;
    width: 710px; height: 141px;
    background: var(--green-box);
    color: var(--green-text);
    font-weight: 600;
    font-size: 18.5px;
    line-height: 26px;
    text-align: center;
    padding-top: 10px;
  }
  .offer {
    position: absolute;
    left: 71px; width: 712px;
    text-align: center;
    font-weight: 700;
    white-space: nowrap;
  }
  .offer.light { color: var(--light-text); text-shadow: 1px 2px 2px rgba(120,50,0,0.45); }
  .offer.dark { color: var(--dark-text); }
  .offer-intro { top: 664px; font-size: 32px; }
  .offer-main { top: 716px; font-size: 49px; font-weight: 600; }
  .offer-place { top: 788px; font-size: 27px; font-weight: 600; }
  .offer-sehri { top: 834px; font-size: 42px; }
  .offer-lecture { top: 936px; font-size: 22px; line-height: 28px; }
  .icon-badge {
    position: absolute; left: 75px;
    width: 62px; height: 62px; border-radius: 50%;
    background: var(--white);
    display: flex; align-items: center; justify-content: center;
  }
  .icon-info { top: 991px; }
  .icon-phone { top: 1108px; }
  .account {
    position: absolute;
    left: 163px; top: 990px; width: 620px;
    color: var(--white);
    font-size: 15px; line-height: 21px;
    font-weight: 400;
  }
  .contact {
    position: absolute;
    left: 163px; top: 1102px; width: 620px;
    color: var(--light-text);
    font-size: 31px; line-height: 38px;
    letter-spacing: 0.5px;
  }
</style>
</head>
<body>
<main class="poster">
  <div class="backdrop-pattern" role="img" aria-label="Soft beige interlocking geometric Islamic pattern background"></div>
  <div class="mosque-silhouette" role="img" aria-label="Orange silhouette of a mosque with domes, minarets and a crescent"></div>

  <div class="brand">
    <span class="brand-dot"></span>
    <span class="brand-name">Noorbel</span>
  </div>

  <div class="panel"></div>

  <h1 class="headline">We are promoting to start an<br>Iftari Program for Ramazan</h1>

  <blockquote class="hadith">
    Whoever offers meal to a Muslim at the time of iftar they receives<br>
    as much reward as that Muslim has earned. Nothing becomes less<br>
    of the reward of those offered meal to.<br>
    (Qaswarî,Sawm: 82; Ibn-i Rashkar, Siyam: 40)"
  </blockquote>

  <p class="offer light offer-intro">We will be giving</p>
  <p class="offer dark offer-main">Iftaris &amp; Dinner</p>
  <p class="offer light offer-place">in different Masajids in Karachi</p>
  <p class="offer dark offer-sehri">Last 10 nights Sehri also</p>
  <p class="offer light offer-lecture">Iftari will be followed with a lecture to motivate<br>INCLUDE THIS ON TOP "</p>

  <div class="icon-badge icon-info">
    <svg width="40" height="44" viewBox="0 0 40 44" aria-hidden="true">
      <circle cx="22" cy="7" r="5" fill="#ef7b30"/>
      <path d="M14 17 h13 l-6 20 h6 l-1 4 h-14 l6 -20 h-5 z" fill="#ef7b30"/>
    </svg>
  </div>
  <p class="account">02930700416781 Noorbel Trust - Sadqa Qardosh Bank Limited, Gulmarvi Branch, Karachi. Once deposited please email us at donations@noorbel.pk so that we can provide you with an official receipt.</p>

  <div class="icon-badge icon-phone">
    <svg width="44" height="44" viewBox="0 0 44 44" aria-hidden="true">
      <circle cx="22" cy="22" r="19" fill="none" stroke="#ef7b30" stroke-width="3"/>
      <path d="M15 12 l5 -1 l3 7 l-3 2 q2 5 6 7 l2 -3 l7 3 l-1 5 q-3 2 -7 1 q-10 -4 -13 -14 q-1 -4 1 -7 z" fill="#ef7b30"/>
    </svg>
  </div>
  <p class="contact">Sameer Hotak +92 321 5580634 for further details</p>
</main>
</body>
</html>
```